Willowmere Counseling (Endure - Mend - Flourish) - Double Sided Business Card

I would like a 2-sided business card. Front: Matte Black or Navy with Logo & Tagline. Back: Name, Address, Phone Number, Email, & Website (maybe would like to include a small map pin-pointing location); Prefer front to be a gold/silver foil (iridescent); Back prefer white or light colored background with lettering that is easy to read and simple

Target Market(s)

Individuals & Couples (13 y.o. - ALL Adults); High end clientele

Industry/Entity Type

Licensed Professional Counselor (Mental Health)

Contact Information for Business Card

Name: Willowmere Counseling; Tagline: Endure - Mend - Flourish; Address: 3870 N. Garrick Ave., Suite 214, Fort Worth, TX 76132; Phone: (214) 555-0187; Website: www.WillowmereCounseling.example

Font styles to use
Serif

Requirements
Must have
• Logo on Front (Large) prefer gold/silver foil on a matte dark color (i.e. black, navy, etc.); Back of Card: All other relevant information

```html
<!DOCTYPE html>
<html lang="en">
<head>
<meta charset="utf-8">
<title>Willowmere Counseling – Business Card</title>
<link rel="stylesheet" href="https://fonts.googleapis.com/css2?family=Cinzel:wght@400;500&family=Crimson+Text:wght@400;600&display=swap">
<style>
  :root {
    --page-bg: #ececec;
    --card-grey: #86878a;
    --card-white: #ffffff;
    --gold: #c9a646;
    --ink-grey: #6d6e71;
    --silver-ink: #2a2a2c;
    --line-grey: #8a8b8e;
    --contact-text: #ffffff;
  }
  * { box-sizing: border-box; margin: 0; padding: 0; }
  html, body { width: 1200px; height: 800px; overflow: hidden; }
  body {
    background: var(--page-bg);
    display: flex;
    align-items: center;
    justify-content: center;
    gap: 40px;
    font-family: "Crimson Text", Georgia, serif;
  }
  .card {
    width: 545px;
    height: 312px;
    border-radius: 22px;
    overflow: hidden;
    position: relative;
    box-shadow: 0 6px 20px rgba(0,0,0,0.15);
  }

  /* Front */
  .card-front {
    background: var(--card-grey);
    display: flex;
    align-items: center;
    justify-content: center;
  }
  .brand {
    display: flex;
    flex-direction: column;
    align-items: center;
    text-align: center;
  }
  .brand-name {
    font-family: "Cinzel", "Times New Roman", serif;
    font-weight: 500;
    letter-spacing: 0.04em;
    line-height: 1.05;
    text-transform: uppercase;
  }
  .brand-rule {
    height: 1.5px;
    margin: 8px 0 6px;
  }
  .brand-tagline {
    font-family: "Cinzel", "Times New Roman", serif;
    text-transform: uppercase;
    letter-spacing: 0.12em;
  }
  .card-front .brand-name { color: var(--silver-ink); font-size: 34px; }
  .card-front .brand-rule { width: 300px; background: var(--silver-ink); }
  .card-front .brand-tagline { color: var(--silver-ink); font-size: 12px; }

  /* Back */
  .card-back { background: var(--card-white); }
  .back-top {
    position: absolute;
    inset: 0 0 96px 0;
  }
  .brand-back {
    position: absolute;
    right: 34px;
    top: 70px;
  }
  .card-back .brand-name { color: var(--gold); font-size: 26px; }
  .card-back .brand-rule { width: 230px; background: var(--ink-grey); }
  .card-back .brand-tagline { color: var(--gold); font-size: 9.5px; }

  .holder {
    position: absolute;
    left: 40px;
    top: 120px;
  }
  .holder-name {
    font-family: "Cinzel", "Times New Roman", serif;
    color: var(--ink-grey);
    font-size: 20px;
    letter-spacing: 0.06em;
    text-transform: uppercase;
  }
  .holder-role {
    font-family: "Cinzel", "Times New Roman", serif;
    color: var(--gold);
    font-size: 15px;
    letter-spacing: 0.05em;
    text-transform: uppercase;
  }

  .divider-gold, .divider-grey {
    position: absolute;
    left: 0; right: 0;
    height: 3px;
  }
  .divider-grey { bottom: 102px; background: var(--line-grey); }
  .divider-gold { bottom: 96px; background: var(--gold); }

  .back-band {
    position: absolute;
    left: 0; right: 0; bottom: 0;
    height: 93px;
    background: var(--card-grey);
    display: flex;
    justify-content: space-between;
    align-items: center;
    padding: 0 30px 0 34px;
    color: var(--contact-text);
    font-size: 13px;
  }
  .contact-list { list-style: none; display: flex; flex-direction: column; gap: 3px; }
  .contact-item { display: flex; align-items: center; gap: 8px; }
  .contact-item svg { width: 12px; height: 12px; flex: none; }
  .address { display: flex; gap: 8px; align-items: flex-start; line-height: 1.3; }
  .address svg { width: 12px; height: 15px; margin-top: 2px; flex: none; }
</style>
</head>
<body>

<section class="card card-front" aria-label="Card front">
  <div class="brand">
    <div class="brand-name">Willowmere<br>Counseling</div>
    <div class="brand-rule"></div>
    <div class="brand-tagline">Endure - Mend - Flourish</div>
  </div>
</section>

<section class="card card-back" aria-label="Card back">
  <div class="back-top">
    <div class="holder">
      <div class="holder-name">Elena Marsh</div>
      <div class="holder-role">CEO/Founder</div>
    </div>
    <div class="brand brand-back">
      <div class="brand-name">Willowmere<br>Counseling</div>
      <div class="brand-rule"></div>
      <div class="brand-tagline">Endure - Mend - Flourish</div>
    </div>
  </div>

  <div class="divider-grey"></div>
  <div class="divider-gold"></div>

  <div class="back-band">
    <ul class="contact-list">
      <li class="contact-item">
        <svg viewBox="0 0 12 12"><path d="M3 1 L5 3.5 L3.8 5 Q5 7.5 7 8.2 L8.5 7 L11 9 L9.5 11 Q3.5 10 1 2.5 Z" fill="var(--gold)"/></svg>
        <span>(214) 555-0187</span>
      </li>
      <li class="contact-item">
        <svg viewBox="0 0 12 12"><rect x="0.5" y="2" width="11" height="8" fill="var(--gold)"/><path d="M0.5 2 L6 6.5 L11.5 2" fill="none" stroke="var(--card-grey)" stroke-width="1"/></svg>
        <span>hello@WillowmereCounseling.example</span>
      </li>
      <li class="contact-item">
        <svg viewBox="0 0 12 12"><circle cx="6" cy="6" r="5" fill="none" stroke="var(--gold)" stroke-width="1.2"/><ellipse cx="6" cy="6" rx="2.2" ry="5" fill="none" stroke="var(--gold)" stroke-width="1"/><path d="M1 6 H11" stroke="var(--gold)" stroke-width="1"/></svg>
        <span>www.WillowmereCounseling.example</span>
      </li>
    </ul>
    <div class="address">
      <svg viewBox="0 0 12 15"><path d="M6 0.5 A5 5 0 0 1 11 5.5 C11 9 6 14.5 6 14.5 C6 14.5 1 9 1 5.5 A5 5 0 0 1 6 0.5 Z" fill="var(--gold)"/><circle cx="6" cy="5.5" r="2" fill="var(--card-grey)"/></svg>
      <span>3870 N. Garrick Ave., Suite 214<br>Fort Worth, TX 76132</span>
    </div>
  </div>
</section>

</body>
</html>
```